Tozvar new design for business cards we want to change our existing design. Logo must remain the same

Hello we are the company TozVar and offer various services regarding transportation and disposal. In addition to our main acquisition of van rental, we also offer disposal and express transportation, so we need new business card designs for our business. Our elders have their time and do not like it anymore. We want to change our existing design. Logo must remain the same as well as the color blue, whether dark or light Does not play a big role in the best medium blue. Logo must be present on the front side. As well as telephone, email, web and location. Big enough but not too big. Back can be redesigned Logo as well as name TozVar must be present. Important is the text: Van rental Disposal and clearing express transportation. Without bail in red should be noted somewhere. it should be modern but not too playful. rather serious but no beating company Thank you very much

Target Market(s)

Private customers as well as companies we want to change our existing design. Logo must remain the same as well as the color blue, whether dark or light Does not play a big role in the best medium blue. Logo must be present on the front side. As well as telephone, email, web and location. Big enough but not too big. Back can be redesigned Logo as well as name TozVar must be present. Important is the text: Van rental Disposal and clearing express transportation. Without bail in red should be noted somewhere. it should be modern but not too playful. rather serious but no beating company Thank you very much

Industry/Entity Type

Car Rental

Contact Information for Business Card

we want to change our existing design. Logo must remain the same as well as the color blue, whether dark or light Does not play a big role in the best medium blue.
Logo must be present on the front side.
As well as telephone, email, web and location. Big enough but not too big.
Back can be redesigned Logo as well as name TozVar must be present.
Important is the text:
Van rental
Disposal and clearing
Express transportation.
Without bail in red should be noted somewhere.
it should be modern but not too playful. rather serious but no beating company
Thank you very much

Font styles to use
Sans Serif

Colors
33a6d7
ec1f27
0692cd
3277b5

Requirements
Must have
• logo and name TozVar as described in the above text must have it. we want to change our existing design. Logo must remain the same as well as the color blue, whether dark or light Does not play a big role in the best medium blue. Logo must be present on the front side. As well as telephone, email, web and location. Big enough but not too big. Back can be redesigned Logo as well as name TozVar must be present. Important is the text: Van rental Disposal and clearing express transportation. Without bail in red should be noted somewhere. it should be modern but not too playful. rather serious but no beating company Thank you very much
Nice to have
• see description we want to change our existing design. Logo must remain the same as well as the color blue, whether dark or light Does not play a big role in the best medium blue. Logo must be present on the front side. As well as telephone, email, web and location. Big enough but not too big. Back can be redesigned Logo as well as name TozVar must be present. Important is the text: Van rental Disposal and clearing express transportation. Without bail in red should be noted somewhere. it should be modern but not too playful. rather serious but no beating company Thank you very much
Should not have
• Blue White and little red we want to change our existing design. Logo must remain the same as well as the color blue, whether dark or light Does not play a big role in the best medium blue. Logo must be present on the front side. As well as telephone, email, web and location. Big enough but not too big. Back can be redesigned Logo as well as name TozVar must be present. Important is the text: Van rental Disposal and clearing express transportation. Without bail in red should be noted somewhere. it should be modern but not too playful. rather serious but no beating company Thank you very much

```html
<!DOCTYPE html>
<html lang="en">
<head>
<meta charset="utf-8">
<title>TozVar Business Cards</title>
<link href="https://fonts.googleapis.com/css2?family=Roboto:wght@400;500;700;900&display=swap" rel="stylesheet">
<style>
  :root {
    --navy: #020066;
    --steel: #7d90b0;
    --paper: #f3f3f3;
    --ink: #4a4a4a;
    --red: #e3141c;
    --white: #ffffff;
    --stage: #dcdcdc;
    --faint: #e3e3ee;
  }
  * { margin: 0; padding: 0; box-sizing: border-box; }
  html, body { width: 1200px; height: 960px; overflow: hidden; }
  body { background: var(--stage); font-family: "Roboto", sans-serif; position: relative; }

  .card { position: absolute; width: 600px; height: 341px; overflow: hidden; }
  .card-front { left: 302px; top: 130px; background: var(--paper); }
  .card-back { left: 299px; top: 489px; background: var(--navy); }

  .front-panel { position: absolute; left: 0; top: 14px; width: 240px; height: 312px; background: var(--faint); }

  .wordmark { position: absolute; display: flex; align-items: center; font-family: "Roboto", sans-serif; font-weight: 900; letter-spacing: 1px; }
  .wordmark-mark { display: block; }
  .card-front .wordmark { left: 298px; top: 60px; font-size: 40px; color: var(--navy); gap: 12px; }
  .card-front .wordmark-mark { width: 22px; height: 22px; background: var(--navy); }
  .card-back .wordmark { left: 142px; top: 126px; font-size: 54px; color: var(--white); gap: 16px; }
  .card-back .wordmark-mark { width: 30px; height: 30px; background: var(--white); }

  .person { position: absolute; left: 58px; top: 216px; }
  .person-name { font-weight: 700; font-size: 21px; color: var(--navy); letter-spacing: 0.3px; }
  .person-role { font-size: 15px; color: var(--steel); margin-top: 2px; }

  .contact { position: absolute; left: 376px; top: 188px; list-style: none; color: var(--ink); font-size: 14.5px; line-height: 18.5px; }
  .contact li { display: flex; align-items: flex-start; gap: 9px; }
  .contact li.address { margin-bottom: 8px; }
  .contact svg { width: 13px; height: 13px; margin-top: 3px; flex: none; fill: var(--navy); }

  .services { position: absolute; left: 0; right: 0; top: 277px; text-align: center; color: var(--white); font-size: 14.5px; }
  .services .dot { display: inline-block; width: 5px; height: 5px; border-radius: 50%; background: var(--white); vertical-align: middle; margin: 0 3px; }
  .no-deposit { position: absolute; left: 0; right: 0; top: 299px; text-align: center; color: var(--red); font-size: 14.5px; }
</style>
</head>
<body>

<section class="card card-front">
  <div class="front-panel" role="img" aria-label="Faint oversized brand symbol decoration"></div>

  <div class="wordmark"><span class="wordmark-mark"></span>TOZVAR</div>

  <div class="person">
    <p class="person-name">LUCA BRENNER</p>
    <p class="person-role">CEO/FOUNDER</p>
  </div>

  <ul class="contact">
    <li class="address">
      <svg viewBox="0 0 24 24"><path d="M12 1a8 8 0 0 0-8 8c0 6 8 14 8 14s8-8 8-14a8 8 0 0 0-8-8zm0 11a3 3 0 1 1 0-6 3 3 0 0 1 0 6z"/></svg>
      <span>Lindenweg 7<br>9300 Seedorf</span>
    </li>
    <li>
      <svg viewBox="0 0 24 24"><path d="M6.6 10.8a15.1 15.1 0 0 0 6.6 6.6l2.2-2.2c.3-.3.7-.4 1-.2 1.1.4 2.3.6 3.6.6.6 0 1 .4 1 1V20c0 .6-.4 1-1 1A17 17 0 0 1 3 4c0-.6.4-1 1-1h3.5c.6 0 1 .4 1 1 0 1.3.2 2.5.6 3.6.1.3 0 .7-.2 1z"/></svg>
      <span>+41 70 555 01 23</span>
    </li>
    <li>
      <svg viewBox="0 0 24 24"><path d="M2 5h20v14H2z" fill="none"/><path d="M2 5h20v2l-10 6L2 7zM2 9l10 6 10-6v10H2z"/></svg>
      <span>info@tozvar.ch</span>
    </li>
    <li>
      <svg viewBox="0 0 24 24"><path d="M12 2a10 10 0 1 0 0 20 10 10 0 0 0 0-20zm6.9 6h-3a15 15 0 0 0-1.3-3.9A8 8 0 0 1 18.9 8zM12 4c.8 1.2 1.5 2.5 1.9 4h-3.8c.4-1.5 1.1-2.8 1.9-4zM4.3 14a8 8 0 0 1 0-4h3.4a16 16 0 0 0 0 4zm.8 2h3a15 15 0 0 0 1.3 3.9A8 8 0 0 1 5.1 16zm3-8h-3a8 8 0 0 1 4.3-3.9A15 15 0 0 0 8.1 8zM12 20c-.8-1.2-1.5-2.5-1.9-4h3.8c-.4 1.5-1.1 2.8-1.9 4zm2.3-6H9.7a14 14 0 0 1 0-4h4.6a14 14 0 0 1 0 4zm.3 5.9a15 15 0 0 0 1.3-3.9h3a8 8 0 0 1-4.3 3.9zm1.7-5.9a16 16 0 0 0 0-4h3.4a8 8 0 0 1 0 4z"/></svg>
      <span>www.TozVar.ch</span>
    </li>
  </ul>
</section>

<section class="card card-back">
  <div class="wordmark"><span class="wordmark-mark"></span>TOZVAR</div>
  <p class="services">Van rental<span class="dot"></span>Disposal &amp; clearing<span class="dot"></span>Express transportation</p>
  <p class="no-deposit">Without bail</p>
</section>

</body>
</html>
```